Verlune Magician

I want the business card for my business to give to people who watch that later I will be employed to show magic here is my website http://www.verlunemagicien-exemple.fr/I want the interesting design , i am very opened for formal and informal, I watch a lot of design so don't stick to the common shape and form but i hope it can also be produced the thing to write on will be the same as in picture that i will upload , i also will upload the logo for you that so can be easy to useDenis CostilleMagicianMAGICIAN VERLUNE 17 rue des Tilleuls - 70400 MONTRÉVAL contact@verlunemagicien-exemple.fr tel. 0372 476 093 tel. 0664 219 570

```html
<!DOCTYPE html>
<html lang="fr">
<head>
<meta charset="utf-8">
<title>Verlune Magicien – carte de visite</title>
<link rel="stylesheet" href="https://fonts.googleapis.com/css2?family=Jost:wght@300&family=Roboto+Condensed:wght@400&display=swap">
<style>
  :root {
    --stage: #2a2a2c;
    --card-white: #ffffff;
    --ink: #111111;
    --back-black: #141414;
    --back-swirl: #2c2c2c;
    --type-white: #f4f4f4;
    --suit-red: #d0202a;
  }
  * { margin: 0; padding: 0; box-sizing: border-box; }
  html, body { width: 1200px; height: 1108px; overflow: hidden; }
  body { background: var(--stage); position: relative; }

  .card {
    position: absolute;
    top: 224px;
    width: 420px;
    height: 660px;
    border-radius: 22px;
    background: var(--card-white);
  }
  .card--front { left: 150px; }
  .card--back  { left: 630px; padding: 18px; }

  .corner {
    position: absolute;
    display: flex;
    flex-direction: column;
    align-items: center;
    font-family: "Jost", sans-serif;
    font-weight: 300;
    color: var(--ink);
    line-height: 1;
  }
  .corner__rank { font-size: 44px; }
  .corner__suit { width: 22px; height: 24px; margin-top: 4px; }
  .corner--top { top: 22px; left: 22px; }
  .corner--bottom { bottom: 22px; right: 22px; transform: rotate(180deg); }

  .portrait {
    position: absolute;
    left: 90px;
    top: 170px;
    width: 240px;
    height: 270px;
    border-radius: 60px 60px 8px 8px;
    background: linear-gradient(180deg, #1c1c1c 0%, #0a0a0a 100%);
  }

  .brand {
    position: absolute;
    left: 0;
    right: 0;
    top: 456px;
    display: flex;
    align-items: center;
    justify-content: center;
    gap: 10px;
    font-family: "Jost", sans-serif;
    font-weight: 300;
    color: var(--ink);
  }
  .brand__name { font-size: 32px; letter-spacing: 1.5px; line-height: 1; white-space: nowrap; }
  .brand__mark {
    width: 8px; height: 8px;
    border-radius: 50%;
    background: var(--suit-red);
    flex: none;
  }

  .back-panel {
    width: 100%;
    height: 100%;
    border-radius: 4px;
    background: radial-gradient(ellipse at 50% 50%, var(--back-swirl) 0%, var(--back-black) 75%);
    display: flex;
    align-items: center;
    justify-content: center;
  }
  .contact {
    text-align: center;
    font-family: "Roboto Condensed", sans-serif;
    font-weight: 400;
    color: var(--type-white);
    font-size: 19px;
    line-height: 1.32;
    letter-spacing: 0.5px;
    font-style: normal;
  }
  .contact__studio { font-size: 18px; }
  .contact__name { font-size: 25px; letter-spacing: 1px; }
</style>
</head>
<body>
  <section class="card card--front" aria-label="Recto">
    <div class="corner corner--top">
      <span class="corner__rank">A</span>
      <svg class="corner__suit" viewBox="0 0 22 24" aria-hidden="true"><path d="M11 0 C15 6 22 9 22 15 C22 19 17 21 13 18 L15 24 H7 L9 18 C5 21 0 19 0 15 C0 9 7 6 11 0Z" fill="#111"/></svg>
    </div>
    <div class="portrait" role="img" aria-label="Illustration en noir et blanc du magicien tenant une carte"></div>
    <div class="brand">
      <span class="brand__name">VERLUNE MAGICIEN</span>
      <span class="brand__mark"></span>
    </div>
    <div class="corner corner--bottom">
      <span class="corner__rank">A</span>
      <svg class="corner__suit" viewBox="0 0 22 24" aria-hidden="true"><path d="M11 0 C15 6 22 9 22 15 C22 19 17 21 13 18 L15 24 H7 L9 18 C5 21 0 19 0 15 C0 9 7 6 11 0Z" fill="#111"/></svg>
    </div>
  </section>

  <section class="card card--back" aria-label="Verso">
    <div class="back-panel" role="img" aria-label="Fond noir à motif d'arabesques gris foncé">
      <address class="contact">
        <div class="contact__studio">MarbecMagician</div>
        <div class="contact__name">MAGICIAN VERLUNE</div>
        <div>17 rue des Tilleuls</div>
        <div>70400 MONTRÉVAL</div>
        <div>contact@verlunemagicien-exemple.fr</div>
        <div>Tel. 0372 476 093</div>
        <div>Tel. 0664 219 570</div>
      </address>
    </div>
  </section>
</body>
</html>
```